Pralivex Website Wordpress Template

For the website of the Pralivex company, a Wordpress template is to be built for one of the main pages and 3 different landing pages. The design has already been finalized and can be seen in the file 200831_PX_Landingpage. In addition, a location finder is to be installed so that the nearest pharmacy that Pralivex sells can be found. The pictures for the slider have already been uploaded. The texts on the main page can be seen in TextChocomedLandingpageallg.pdf. The texts of the target group landing pages can be seen under TextChocomedDifferentLandingpage.pdf. An imprint page is to be implemented, but will be filled at a later date.

For the website of the company Pralivex a WordPress template for one main page and 3 different landing pages is to be built. The design is already finalized and can be seen in the file 200831_PX_Landingpage. In addition, a store finder should be installed via which the nearest pharmacy, which Pralivex distributes, can be found. The images for the sliders are already uploaded. The texts of the main page is described in TextChocomedLandingpageallg.pdf. The texts of the target group landing pages can be found under TextChocomedDifferentLandingpage.pdf. An imprint page is to be implemented, but will be filled at a later stage.

```html
<!DOCTYPE html>
<html lang="de">
<head>
<meta charset="utf-8">
<title>Pralivex – Schokolade statt Tabletten</title>
<link href="https://fonts.googleapis.com/css2?family=Roboto+Slab:wght@300;400;500;700&display=swap" rel="stylesheet">
<style>
:root{
  --olive:#76754a;
  --olive-text:#6d6f3e;
  --olive-light:#b8b89e;
  --brown:#6b3530;
  --sand:#f1f0ec;
  --panel:#efeeea;
  --white:#ffffff;
  --ink:#555548;
}
*{box-sizing:border-box;margin:0;padding:0}
html,body{width:1200px;height:2973px;overflow:hidden}
body{font-family:"Roboto Slab",serif;background:var(--white);color:var(--olive-text);position:relative;border-top:3px solid var(--brown)}
.abs{position:absolute}
.brand{left:111px;top:30px;display:flex;align-items:center;gap:12px}
.brand-square{width:40px;height:40px;background:var(--brown)}
.brand-name{font-size:34px;font-weight:700;color:var(--brown);letter-spacing:1px}
.tagline{right:113px;top:32px;text-align:right;font-size:18px;line-height:34px}
.tagline strong{font-weight:500}
.tagline span{font-weight:300}
.hero-title{left:111px;top:292px;font-size:56px;line-height:68px;font-weight:700;color:var(--olive-text)}
.hero-visual{left:520px;top:200px;width:680px;height:500px;background:linear-gradient(160deg,#e2c53c 0%,#8e914e 45%,#7b4a34 80%,#ffffff 100%);border-radius:4px}
.slider-dots{left:111px;top:602px;display:flex;gap:8px;align-items:center}
.slider-dots i{display:block;width:13px;height:13px;border-radius:50%;background:var(--olive-text)}
.slider-dots i.active{background:none;border:2px solid var(--olive-text);width:17px;height:17px}
.intro{left:200px;top:738px;width:800px;text-align:center;font-size:22px;line-height:34.5px;font-weight:500}
.finder{left:0;top:1063px;width:1200px;height:699px;background:var(--olive)}
.finder-title{left:0;top:1122px;width:1200px;text-align:center;font-size:36px;font-weight:400;color:var(--white)}
.finder-title b{font-weight:700}
.finder-search{left:285px;top:1193px;width:631px;height:55px;border-radius:28px;background:var(--white);color:var(--olive-text);font-size:17px;font-weight:700;display:flex;align-items:center;justify-content:center}
.locator{left:111px;top:1285px;width:978px;height:380px;display:flex;box-shadow:0 2px 8px rgba(0,0,0,.15)}
.locator-list{width:343px;background:var(--panel);padding:36px 18px 0}
.locator-list h3{text-align:center;font-size:17px;font-weight:700;margin-bottom:16px}
.pharmacy{background:var(--white);height:115px;display:flex;padding:8px 8px;gap:18px;margin-bottom:13px;box-shadow:0 1px 3px rgba(0,0,0,.1)}
.pharmacy-photo{width:100px;height:100px;flex:none;background:linear-gradient(135deg,#6b4a2c,#c9a06a,#d9517a)}
.pharmacy-photo.room{background:linear-gradient(135deg,#b8b2a6,#ece8e2,#8a857c)}
.pharmacy p{font-size:16px;line-height:26px;color:var(--ink);font-weight:300;margin-top:2px}
.pharmacy small{font-size:9px;color:var(--ink);display:flex;align-items:center;gap:3px}
.locator-map{flex:1;background:linear-gradient(120deg,#f7f1de 0%,#f3ecd2 60%,#d6e4f7 88%,#a9c6f3 100%)}
.faq{left:183px;width:834px;color:var(--white)}
.faq-item{position:absolute;left:0;width:834px;background:var(--olive-light);padding:30px 110px 0 37px}
.faq-item h4{font-size:22px;line-height:34px;font-weight:400;text-transform:uppercase}
.faq-item.open{background:var(--olive);padding-top:28px}
.faq-item.open p{font-size:14.5px;line-height:25.5px;margin-top:20px;font-weight:400}
.faq-item svg{position:absolute;right:34px;top:48px}
.footer{left:0;top:2630px;width:1200px;height:343px;background:var(--sand)}
.footer-col{top:2697px;font-size:18px;line-height:26px;font-weight:300;color:var(--olive-text)}
.footer-col h5{font-size:21px;font-weight:500;margin-bottom:24px}
.imprint{left:821px;top:2697px;width:189px;height:45px;border-radius:23px;background:var(--olive);color:var(--white);font-size:14px;font-weight:700;display:flex;align-items:center;justify-content:center}
</style>
</head>
<body>
<header>
  <div class="abs brand"><span class="brand-square"></span><span class="brand-name">PRALIVEX</span></div>
  <div class="abs tagline"><strong>Weltneuheit aus Österreich!</strong><br><span>Feine Milchschokolade mit dem wertvollen Extrakt von Oliven.</span></div>
</header>

<section class="hero">
  <h1 class="abs hero-title">Schokolade statt<br>Tabletten.</h1>
  <div class="abs hero-visual" role="img" aria-label="Produktverpackung mit Milchschokolade und Olivenextrakt, davor einzelne Schokoladenstücke"></div>
  <div class="abs slider-dots"><i class="active"></i><i></i><i></i><i></i></div>
</section>

<p class="abs intro">PRALIVEX hat die mediterrane Ernährung mit all ihren Vorteilen „komprimiert“ und in eine gesunde Süßigkeit gepackt. Die wichtigste Zutat: Oliven. Aus 240 kg davon gewinnt man 1 kg Oliven-Extrakt, welches von uns in hochwertige Schokolade eingearbeitet wird. Das ist die neue Art der Nahrungsergänzung: konsumiert man täglich drei Mini-Stückchen Schokolade, nimmt man garantiert 5 mg wertvolle, gesundheitsfördernde Polyphenole der Olive zu sich.</p>

<section class="abs finder"></section>
<h2 class="abs finder-title">Jetzt <b>PRALIVEX</b> in der Apotheke gratis testen!</h2>
<div class="abs finder-search">Postleitzahl eingeben und nächste teilnehmende Apotheke finden</div>
<div class="abs locator">
  <div class="locator-list">
    <h3>NEAREST PHARMACY</h3>
    <div class="pharmacy">
      <div class="pharmacy-photo" role="img" aria-label="Foto der Apotheke mit Gebäckauslage"></div>
      <div><p>Lorem ipsum dolor sit amet, consectetur adi piscingLorem</p><small><svg width="8" height="8" viewBox="0 0 8 8"><circle cx="4" cy="4" r="3.3" fill="none" stroke="#555548"/><path d="M4 2v2h1.5" stroke="#555548" fill="none"/></svg>15min</small></div>
    </div>
    <div class="pharmacy">
      <div class="pharmacy-photo room" role="img" aria-label="Foto des Apothekenraums"></div>
      <div><p>Lorem ipsum dolor sit amet, consectetur adi piscingLorem</p><small><svg width="8" height="8" viewBox="0 0 8 8"><circle cx="4" cy="4" r="3.3" fill="none" stroke="#555548"/><path d="M4 2v2h1.5" stroke="#555548" fill="none"/></svg>15min</small></div>
    </div>
  </div>
  <div class="locator-map" role="img" aria-label="Stadtplan mit Standorten der teilnehmenden Apotheken"></div>
</div>

<section class="abs faq">
  <div class="faq-item open" style="top:1860px;height:289px">
    <h4>Wie ist Pralivex entstanden, wer hat es entwickelt und wer produziert es?</h4>
    <p>Lorem ipsum dolor sit amet, consectetur adipiscing elit, sed do eiusmod tempor incididunt ut labore et dolore magna aliqua. Ut enim ad minim veniam, quis nostrud exercitation ullamco laboris nisi ut aliquip ex ea commodo consequat. Duis aute irure dolor in reprehenderit in voluptate velit esse cillum dolore eu fugiat nulla Lorem ipsum dolor sit amet, consectetur adipiscing elit, sed do eiusmod tempor incididunt ut labore et dolore magna aliqua. Ut enim ad minim veniam</p>
    <svg width="30" height="18" viewBox="0 0 30 18"><path d="M2 2l13 13L28 2" stroke="#fff" stroke-width="3" fill="none"/></svg>
  </div>
  <div class="faq-item" style="top:2177px;height:101px"><h4>Welche Testresultate gibt es zu Pralivex?</h4><svg width="30" height="18" viewBox="0 0 30 18"><path d="M2 2l13 13L28 2" stroke="#fff" stroke-width="3" fill="none"/></svg></div>
  <div class="faq-item" style="top:2305px;height:101px"><h4>Wie soll Pralivex verwendet werden?</h4><svg width="30" height="18" viewBox="0 0 30 18"><path d="M2 2l13 13L28 2" stroke="#fff" stroke-width="3" fill="none"/></svg></div>
  <div class="faq-item" style="top:2434px;height:101px"><h4>Kann man Pralivex auch Kindern geben?</h4><svg width="30" height="18" viewBox="0 0 30 18"><path d="M2 2l13 13L28 2" stroke="#fff" stroke-width="3" fill="none"/></svg></div>
</section>

<footer>
  <div class="abs footer"></div>
  <div class="abs footer-col" style="left:186px"><h5>PRALIVEX – Büro Wien:</h5>Dr. Lukas Hofer<br>Lindengasse 12/4, A-1010 Wien, Austria,<br>office@pralivex.at ,<br>www.pralivex.at.<br>Erzeugt in Talbach, Tirol.</div>
  <div class="abs footer-col" style="left:589px"><h5>KONTAKT</h5>office@pralivex.at</div>
  <div class="abs imprint">IMPRINT</div>
</footer>
</body>
</html>
```